Professional Oral Surgery Referral Pad, Business Card, and Stationary Design

Hello,

I want to work with a designer for my startup Oral Surgery Practice called: Redmont Creek Oral Surgery & Implant Center

Ideally I would like to choose a good/professional design and work with a designer all the way to fulfill ALL of our stationary needs including referral pads, business cards, letterheads, envelopes, notepads, email signature, etc.

I would like to see designs first and hopefully would like to work with the designer for the lifetime of my practice and wanting to develop a long-term professional relationship.

In terms of the logo I have attached our practice logo files: I want to stay within the 3 colorways of the logo: Navy Blue/Silver grey/White. I would like for you to be creative and incorporate the "V" as best you can (for example greyed out watermark, etc)

I have also attached in my files the full contact info of our office in a word document: which includes address, email address, phone, fax, cell, etc.

I have also attached a few examples of double sided referral pad we can draw inspiration from. In terms of the referral pad I would ideally like to have my logo nicely placed/incorporated to make it look professional, address of the practice and contact info, my name and credentials.

Referral pad must have lines for patient, date of birth, phone number, referring doctor name, odontogram of all adult teeth and pediatric teeth, nice and big - so easy for dentist to refer. Also a jaw drawing of the intraoral cavity. Below that should have comments to surgeon.

In terms of procedures, I would like to have options of IV sedation, extractions, wisdom teeth, bone graft, pathology, tmj, trauma, expose/bond, orthognathic, other (list below)

In the back we can have a greyed out map of my practice address and Instructions for patients should include to bring insurance documentation, medication list, etc.

The final nitty gritty details of the referral pad can be worked on once I am happy with the design.

Target Market(s)

Patients who need oral surgical services and dentist referrals

Industry/Entity Type

Oral and Maxillofacial Surgery

Font styles to use
Other font styles liked:
• I would leave it up to the designers!

Colors
0054AA
0677BA
7BADD7
CADEEF
E8F1F8

Requirements
Must have
• Professional/sleek/modern and three color ways same as logo (navy blue, silver gray, and white)
Nice to have
• I would like to highlight my logo especially the implant ā€œvā€ either as watermark or part of the header or footnote. I will leave it to the expertise of the designer

```html
<!DOCTYPE html>
<html lang="en">
<head>
<meta charset="utf-8">
<title>Redmont Creek Oral Surgery – Referral Pad</title>
<link href="https://fonts.googleapis.com/css2?family=Fira+Sans:ital,wght@0,300;0,400;0,600;0,700;1,300&family=Mulish:ital,wght@1,400&display=swap" rel="stylesheet">
<style>
:root{
  --navy:#0d3f8e;
  --ink:#0a4ca0;
  --blue:#0054aa;
  --pale:#cadeef;
  --mist:#e8f1f8;
  --grey:#5d6470;
  --rule:#7f8ea3;
  --border:#c9ccd1;
  --white:#ffffff;
}
*{box-sizing:border-box;margin:0;padding:0}
html,body{width:1200px;height:1200px;overflow:hidden;background:var(--white)}
body{position:relative;font-family:"Fira Sans",sans-serif;color:var(--ink)}
.sheet{position:absolute;top:219px;width:498px;height:770px;border:1px solid var(--border);background:var(--white)}
.sheet--front{left:92px}
.sheet--back{left:617px}
.abs{position:absolute;white-space:nowrap}

/* header */
.header-band{position:absolute;left:0;top:0}
.brand{position:absolute;left:0;top:66px;width:242px;text-align:center;color:var(--white);font-weight:400;line-height:1.15}
.brand__name{font-size:21px;letter-spacing:.5px}
.brand__sub{font-size:9.5px;letter-spacing:1.2px;text-transform:uppercase;margin-top:4px}
.doctor{left:257px;top:47px;font-size:14.5px;font-weight:700;color:var(--white);line-height:17px}
.contact{left:257px;font-family:"Mulish",sans-serif;font-style:italic;font-size:9.6px;color:var(--grey)}
.contact svg{width:10px;height:10px;vertical-align:-1px;margin-right:6px;fill:var(--navy)}

/* fields */
.field{font-size:13px;font-weight:400;color:var(--ink);line-height:16px}
.rule{position:absolute;height:1px;background:var(--rule)}
.box{position:absolute;width:10px;height:10px;border:1px solid var(--grey)}

/* odontogram */
.mouth{position:absolute;left:42px;top:286px;width:123px;height:183px;border-radius:50%;background:radial-gradient(ellipse at center,var(--mist),var(--pale));border:1.5px solid var(--navy)}
.teeth{position:absolute;background:linear-gradient(180deg,var(--mist),var(--pale));border-radius:6px}
.num{position:absolute;font-size:7.5px;font-weight:700;color:var(--navy);transform:translateX(-50%);line-height:9px}

/* procedures */
.section-title{font-size:13px;font-weight:700;color:var(--ink);line-height:16px}
.item{font-size:12.6px;font-weight:300;color:var(--grey);line-height:15px}

/* back */
.heading{left:22px;font-size:14px;font-weight:400;color:var(--ink);line-height:18px;letter-spacing:.2px}
.copy{position:absolute;left:22px;font-size:10.6px;font-weight:300;color:#3c3f44;line-height:16.6px}
.copy span{display:block;white-space:nowrap}
.copy b{font-weight:600}
.callout{position:absolute;left:0;width:100%;text-align:center;font-size:11.4px;font-weight:700;color:var(--ink);line-height:19.4px;letter-spacing:.3px}
.notice{position:absolute;left:0;width:100%;text-align:center;font-size:10.8px;font-weight:300;color:#3c3f44}
.map{position:absolute;left:90px;top:545px;width:318px;height:181px;background:linear-gradient(135deg,#eef0f3,#d5dae2);border:1px solid #e2e4e8}
.map-address{position:absolute;left:0;width:100%;top:732px;text-align:center;font-size:10.8px;color:var(--ink)}
.map-address svg{width:9px;height:11px;vertical-align:-1px;margin-right:6px;fill:var(--navy)}
</style>
</head>
<body>

<section class="sheet sheet--front" aria-label="Referral slip, front">
  <svg class="header-band" width="498" height="122" viewBox="0 0 498 122" aria-hidden="true">
    <path d="M0 47 H498 V64 H252 Q242 64 242 74 V108 Q242 120 230 120 H0 Z" fill="var(--navy)"/>
  </svg>
  <div class="brand">
    <div class="brand__name">Redmont Creek</div>
    <div class="brand__sub">Oral Surgery &amp; Implant Center</div>
  </div>
  <div class="abs doctor">Dr. Aaron Vale, DDS</div>
  <div class="abs contact" style="top:67px"><svg viewBox="0 0 10 10"><path d="M5 0a3.5 3.5 0 0 0-3.5 3.5C1.5 6 5 10 5 10s3.5-4 3.5-6.5A3.5 3.5 0 0 0 5 0zm0 5a1.4 1.4 0 1 1 0-2.8A1.4 1.4 0 0 1 5 5z"/></svg>180 Alder Crest Ave, Redmont, CA 91000</div>
  <div class="abs contact" style="top:81px"><svg viewBox="0 0 10 10"><path d="M2 0l2 2.5-1 1.2c.6 1.3 1.6 2.3 2.9 2.9l1.2-1L9.6 7.6 8.3 9.6C4 9.3.7 6 .4 1.7z"/></svg>555 201 4480</div>
  <div class="abs contact" style="top:95px"><svg viewBox="0 0 10 10"><path d="M2.5 0h5v2.5h-5zM0 3h10v4.5H8V6H2v1.5H0zM2.5 7h5v3h-5z"/></svg>555 201 4481</div>
  <div class="abs contact" style="top:109px"><svg viewBox="0 0 10 10"><path d="M0 1.5h10v7H0zm1 .9 4 3.1 4-3.1" stroke="var(--white)" stroke-width=".8"/></svg>info@redmontcreekos.com</div>

  <div class="abs field" style="left:23px;top:140px">Introducing</div>
  <div class="rule" style="left:92px;width:263px;top:153px"></div>
  <div class="abs field" style="left:366px;top:140px">Date</div>
  <div class="rule" style="left:397px;width:78px;top:153px"></div>

  <div class="abs field" style="left:23px;top:164px">Patient Phone</div>
  <div class="rule" style="left:105px;width:370px;top:176px"></div>

  <div class="abs field" style="left:23px;top:187px">DOB</div>
  <div class="rule" style="left:52px;width:423px;top:199px"></div>

  <div class="box" style="left:22px;top:213px"></div>
  <div class="abs field" style="left:39px;top:210px">Call to appoint</div>
  <div class="box" style="left:128px;top:213px"></div>
  <div class="abs field" style="left:149px;top:210px">Patient will call</div>
  <div class="box" style="left:246px;top:213px"></div>
  <div class="abs field" style="left:266px;top:210px">Appointment made by referring doctor</div>

  <div class="abs field" style="left:23px;top:233px">Referring Doctor</div>
  <div class="rule" style="left:125px;width:350px;top:247px"></div>

  <div class="abs field" style="left:23px;top:256px">Phone</div>
  <div class="rule" style="left:61px;width:414px;top:268px"></div>

  <div class="mouth" role="img" aria-label="Line drawing of the open mouth showing both dental arches and tongue"></div>

  <div class="teeth" role="img" aria-label="Permanent upper teeth 1 to 16" style="left:179px;top:278px;width:279px;height:38px"></div>
  <div class="teeth" role="img" aria-label="Permanent lower teeth 17 to 32" style="left:179px;top:340px;width:279px;height:29px"></div>
  <div class="teeth" role="img" aria-label="Primary upper teeth A to J" style="left:218px;top:396px;width:198px;height:34px"></div>
  <div class="teeth" role="img" aria-label="Primary lower teeth K to T" style="left:218px;top:435px;width:198px;height:34px"></div>

  <div class="num" style="left:186px;top:318px">1</div><div class="num" style="left:203px;top:318px">2</div><div class="num" style="left:220px;top:318px">3</div><div class="num" style="left:237px;top:318px">4</div><div class="num" style="left:254px;top:318px">5</div><div class="num" style="left:271px;top:318px">6</div><div class="num" style="left:288px;top:318px">7</div><div class="num" style="left:305px;top:318px">8</div>
  <div class="num" style="left:333px;top:318px">9</div><div class="num" style="left:348px;top:318px">10</div><div class="num" style="left:364px;top:318px">11</div><div class="num" style="left:381px;top:318px">12</div><div class="num" style="left:398px;top:318px">13</div><div class="num" style="left:414px;top:318px">14</div><div class="num" style="left:432px;top:318px">15</div><div class="num" style="left:449px;top:318px">16</div>
  <div class="num" style="left:186px;top:331px">32</div><div class="num" style="left:203px;top:331px">31</div><div class="num" style="left:220px;top:331px">30</div><div class="num" style="left:237px;top:331px">29</div><div class="num" style="left:254px;top:331px">28</div><div class="num" style="left:271px;top:331px">27</div><div class="num" style="left:288px;top:331px">26</div><div class="num" style="left:305px;top:331px">25</div>
  <div class="num" style="left:330px;top:331px">24</div><div class="num" style="left:347px;top:331px">23</div><div class="num" style="left:364px;top:331px">22</div><div class="num" style="left:381px;top:331px">21</div><div class="num" style="left:398px;top:331px">20</div><div class="num" style="left:415px;top:331px">19</div><div class="num" style="left:432px;top:331px">18</div><div class="num" style="left:449px;top:331px">17</div>

  <div class="num" style="left:229px;top:384px">A</div><div class="num" style="left:252px;top:384px">B</div><div class="num" style="left:274px;top:384px">C</div><div class="num" style="left:289px;top:384px">D</div><div class="num" style="left:307px;top:384px">E</div><div class="num" style="left:327px;top:384px">F</div><div class="num" style="left:344px;top:384px">G</div><div class="num" style="left:362px;top:384px">H</div><div class="num" style="left:381px;top:384px">I</div><div class="num" style="left:404px;top:384px">J</div>
  <div class="num" style="left:228px;top:470px">T</div><div class="num" style="left:251px;top:470px">S</div><div class="num" style="left:269px;top:470px">R</div><div class="num" style="left:288px;top:470px">Q</div><div class="num" style="left:305px;top:470px">P</div><div class="num" style="left:325px;top:470px">O</div><div class="num" style="left:342px;top:470px">N</div><div class="num" style="left:360px;top:470px">M</div><div class="num" style="left:381px;top:470px">L</div><div class="num" style="left:405px;top:470px">K</div>

  <div class="abs section-title" style="left:23px;top:489px">FACIAL PROCEDURES</div>
  <div class="box" style="left:22px;top:511px"></div><div class="abs item" style="left:36px;top:508px">Orthognathic Evaluation</div>
  <div class="box" style="left:22px;top:530px"></div><div class="abs item" style="left:36px;top:527px">Sleep Apnea</div>
  <div class="box" style="left:22px;top:549px"></div><div class="abs item" style="left:36px;top:546px">TMJ Evaluation</div>
  <div class="box" style="left:22px;top:568px"></div><div class="abs item" style="left:36px;top:565px">Pathology</div>
  <div class="box" style="left:22px;top:587px"></div><div class="abs item" style="left:36px;top:584px">Cleft Lip, Palate Evaluation</div>
  <div class="box" style="left:22px;top:606px"></div><div class="abs item" style="left:36px;top:603px">Facial Trauma</div>
  <div class="box" style="left:22px;top:625px"></div><div class="abs item" style="left:36px;top:622px">Other</div>
  <div class="rule" style="left:75px;width:111px;top:634px"></div>

  <div class="abs section-title" style="left:231px;top:489px">ORAL SURGERY PROCEDURES</div>
  <div class="box" style="left:231px;top:511px"></div><div class="abs item" style="left:246px;top:508px">Extraction, Tooth #</div>
  <div class="rule" style="left:357px;width:118px;top:520px"></div>
  <div class="box" style="left:231px;top:530px"></div><div class="abs item" style="left:246px;top:527px">Wisdom Teeth Removal #</div>
  <div class="rule" style="left:389px;width:86px;top:539px"></div>
  <div class="box" style="left:231px;top:549px"></div><div class="abs item" style="left:246px;top:546px">Evaluation For Implants</div>
  <div class="rule" style="left:380px;width:95px;top:558px"></div>
  <div class="box" style="left:231px;top:568px"></div><div class="abs item" style="left:246px;top:565px">Exposure of Tooth #</div>
  <div class="rule" style="left:358px;width:117px;top:577px"></div>
  <div class="box" style="left:231px;top:587px"></div><div class="abs item" style="left:246px;top:584px">Other</div>
  <div class="rule" style="left:280px;width:195px;top:596px"></div>
  <div class="rule" style="left:231px;width:244px;top:616px"></div>
  <div class="rule" style="left:231px;width:244px;top:636px"></div>

  <div class="abs section-title" style="left:22px;top:650px">Radiographs</div>
  <div class="box" style="left:22px;top:678px"></div><div class="abs item" style="left:36px;top:675px">Emailed: info@redmontcreekos.com</div>
  <div class="box" style="left:22px;top:697px"></div><div class="abs item" style="left:36px;top:694px">Given to Patient</div>
  <div class="box" style="left:22px;top:716px"></div><div class="abs item" style="left:36px;top:713px">Mailed</div>
  <div class="box" style="left:22px;top:735px"></div><div class="abs item" style="left:36px;top:732px">Please Take</div>

  <div class="abs section-title" style="left:231px;top:648px">Notes</div>
  <div class="rule" style="left:270px;width:205px;top:660px"></div>
  <div class="rule" style="left:231px;width:244px;top:682px"></div>
  <div class="rule" style="left:231px;width:244px;top:704px"></div>
  <div class="rule" style="left:231px;width:244px;top:725px"></div>
  <div class="rule" style="left:231px;width:244px;top:747px"></div>
</section>

<section class="sheet sheet--back" aria-label="Referral slip, back">
  <h2 class="abs heading" style="top:43px">INSTRUCTIONS FOR YOUR FIRST VISIT</h2>
  <div class="copy" style="top:64px">
    <span>• Please bring all x-rays, this referral slip, pertinent medical information and a list of ALL</span>
    <span>medications you are currently taking.</span>
    <span>• Please alert the office if you have a medical condition that may be of concern prior to</span>
    <span>surgery. (Bleeding disorders, heart conditions, taking blood thinners, etc.)</span>
    <span>• Please bring a photo ID and both your medical and dental insurance cards on the day of</span>
    <span>your appointment.</span>
    <span>• Patients under eighteen (18) years of age must be accompanied by a parent or legal</span>
    <span>guardian at the time of the initial consult and surgery.</span>
  </div>

  <h2 class="abs heading" style="top:202px">INSTRUCTIONS FOR GENERAL ANESTHESIA</h2>
  <div class="copy" style="top:224px">
    <span><b>PLEASE NOTE:</b> In most instances, sedation and surgery are not performed at the first</span>
    <span>appointment. Typically, the patient is seen first for consultation and surgery is scheduled</span>
    <span>for a separate appointment. <b>The following only applies if surgery with sedation is</b></span>
    <span><b>done at the first appointment:</b></span>
  </div>
  <div class="copy" style="top:296px">
    <span>• Do not eat or drink anything 8 hours prior to your surgery, NO FOOD OR DRINK, including</span>
    <span>water, unless directed by your doctor.</span>
    <span>• Most daily medications may be taken prior to surgery with only a SIP of WATER.</span>
    <span>Please call our office if you have any questions regarding your medications.</span>
    <span>• Any patient under 18 years of age must be accompanied by a parent or legal guardian.</span>
    <span>Wear loose, comfortable clothing with sleeves that can be raised above your elbow. Avoid</span>
    <span>slippers and sandals.</span>
    <span>• If you require corrective lenses, please wear your glasses. No contacts.</span>
  </div>
  <div class="copy" style="top:434px"><span><b>Please call our office with any questions! 555 201 4480</b></span></div>

  <div class="callout" style="top:466px">YOU MUST BE ACCOMPANIED BY SOMEONE TO DRIVE YOU<br>HOME &amp; STAY WITH YOU FOR SIX HOURS AFTER SURGERY</div>
  <div class="notice" style="top:510px">Please give 48 hours notice if you are unable to keep this appointment.</div>

  <div class="map" role="img" aria-label="Greyed street map marking the practice location"></div>
  <div class="map-address"><svg viewBox="0 0 10 12"><path d="M5 0a4 4 0 0 0-4 4c0 3 4 8 4 8s4-5 4-8a4 4 0 0 0-4-4zm0 5.6A1.6 1.6 0 1 1 5 2.4a1.6 1.6 0 0 1 0 3.2z"/></svg>180 Alder Crest Ave, Redmont, CA 91000</div>
</section>

</body>
</html>
```